Church Christmas Flyer

The flyer is to advertise our Christmas Eve services. The flyer is for a Christian church service to celebrate the birth of Jesus. We would like to see designs that use blue, silver and gold for colors but feel free to be creative. We are interested in a flyer that is has texture, depth and is more abstract than literal. Don't be afraid to layer. Please make the flyer double sided

* I uploaded our Christmas flyer from last year.

Target Market(s)

30-55 year old, male and female

Industry/Entity Type

Church

Requirements
Must have
• Map to the church
Church phone number 555-317-4096
Service times 3:00pm and 5:00pm
church address 28315 Marigold Ave, Hesperia, Ca. 92345
church website www.brookfieldfellowshipnt.com
Scripture verse

Text must stand out and be easy to read
Nice to have
• Use of the star in the sky that guided the wise men to Jesus.
Should not have
• Santa Clause, Snowmen, Reindeer

```html
<!DOCTYPE html>
<html lang="en">
<head>
<meta charset="utf-8">
<title>Brookfield Fellowship High Desert – Christmas Eve Flyer</title>
<link rel="stylesheet" href="https://fonts.googleapis.com/css2?family=Questrial&family=Pinyon+Script&display=swap">
<style>
  :root {
    --ink: #000000;
    --night: #0c1628;
    --sky: #1f4f9c;
    --sky-deep: #10244a;
    --ground: #2f6a6e;
    --gold: #e8a323;
    --white: #ffffff;
    --mist: #dfe7ee;
    --blue-word: #3c73c4;
    --teal-word: #5fb5c2;
    --pale-word: #a9d4e6;
    --grey-name: #8a8f96;
    --map-bg: #eef0f2;
    --map-frame: #c9a24a;
  }
  html, body { margin: 0; padding: 0; overflow: hidden; background: var(--ink); }
  .flyer {
    position: relative; width: 1200px; height: 1097px; overflow: hidden;
    background: var(--ink);
    font-family: "Questrial", "Century Gothic", sans-serif;
  }
  .side { position: absolute; left: 0; width: 1200px; height: 548px; }
  .side--front { top: 0; }
  .side--back { top: 549px; }
  .backdrop { position: absolute; }
  .side--front .backdrop {
    left: 0; top: 0; width: 1118px; height: 548px;
    background:
      radial-gradient(ellipse 420px 260px at 230px 120px, var(--sky) 0%, rgba(31,79,156,0) 100%),
      radial-gradient(ellipse 360px 200px at 1050px 60px, rgba(232,163,35,.35) 0%, rgba(232,163,35,0) 100%),
      linear-gradient(180deg, var(--sky-deep) 0%, var(--night) 45%, #123238 75%, var(--ground) 92%, #0d1a1c 100%);
  }
  .side--back .backdrop {
    left: 62px; top: 0; width: 1138px; height: 548px;
    background:
      radial-gradient(ellipse 420px 220px at 1000px 90px, var(--sky) 0%, rgba(31,79,156,0) 100%),
      radial-gradient(ellipse 300px 160px at 140px 70px, rgba(232,163,35,.35) 0%, rgba(232,163,35,0) 100%),
      linear-gradient(180deg, var(--sky-deep) 0%, var(--night) 50%, #0e2026 85%, #1d3f44 100%);
  }
  .star {
    position: absolute; width: 6px; height: 6px; border-radius: 50%;
    background: var(--white); box-shadow: 0 0 10px 4px rgba(255,255,255,.6);
  }
  .text { position: absolute; white-space: nowrap; line-height: 1; }
  .church-name { color: var(--gold); font-size: 53px; right: 105px; top: 64px; }
  .web-small { color: var(--mist); font-size: 17px; left: 395px; top: 126px; }
  .event-title { color: var(--white); font-size: 52px; right: 104px; top: 136px; }
  .event-sub { color: var(--white); font-size: 29px; right: 108px; top: 192px; }
  .verse {
    font-family: "Pinyon Script", cursive; color: var(--white); font-size: 44px;
  }
  .verse .big { font-size: 66px; }
  .verse .mighty { color: var(--blue-word); }
  .verse .delight { color: var(--teal-word); }
  .verse .rejoice, .verse .singing { color: var(--pale-word); }
  .verse--l1 { right: 52px; top: 282px; }
  .verse--l2 { left: 70px; top: 352px; }
  .verse--l3 { right: 52px; top: 422px; }
  .citation { color: var(--mist); font-size: 17px; left: 808px; top: 493px; }

  .service-title { color: var(--white); font-size: 50px; left: 82px; top: 87px; }
  .service-sub { color: var(--white); font-size: 30px; left: 86px; top: 138px; }
  .date { color: var(--gold); font-size: 88px; left: 150px; top: 213px; }
  .times { color: var(--gold); font-size: 52px; left: 345px; top: 318px; }
  .map {
    position: absolute; left: 870px; top: 128px; width: 268px; height: 266px;
    border: 2px solid var(--map-frame);
    background: linear-gradient(135deg, var(--map-bg) 0%, #dfe5ea 100%);
  }
  .addr-name { color: var(--grey-name); font-size: 42px; left: 88px; top: 429px; }
  .addr-line { color: var(--grey-name); font-size: 31px; left: 90px; top: 480px; }
  .web { color: var(--mist); font-size: 22px; left: 863px; top: 444px; }
  .phone { color: var(--white); font-size: 32px; left: 900px; top: 482px; }
</style>
</head>
<body>
<main class="flyer">
  <section class="side side--front">
    <div class="backdrop" role="img" aria-label="Textured night sky with the guiding star, golden light streaks and a dim desert landscape"></div>
    <span class="star" style="left:187px;top:85px"></span>
    <div class="text church-name">Brookfield Fellowship High Desert</div>
    <div class="text web-small">www.brookfieldfellowshipnt.com</div>
    <div class="text event-title">Christmas Eve</div>
    <div class="text event-sub">A Celebration of God’s love</div>
    <div class="text verse verse--l1">“The Lord your God is with you, he is <span class="big mighty">mighty</span> to save.</div>
    <div class="text verse verse--l2">He will take great <span class="big delight">delight</span> in you, he will quiet you with his <span class="big">love</span>,</div>
    <div class="text verse verse--l3">he will <span class="big rejoice">rejoice</span> over you with <span class="big singing">singing</span>.”</div>
    <div class="text citation">Zephaniah 3:17</div>
  </section>

  <section class="side side--back">
    <div class="backdrop" role="img" aria-label="Textured night sky with the guiding star and golden light streaks"></div>
    <span class="star" style="left:991px;top:85px"></span>
    <div class="text service-title">Christmas Eve Service</div>
    <div class="text service-sub">A Celebration of God’s love</div>
    <div class="text date">December 24th</div>
    <div class="text times">3:00pm &amp; 5:00pm</div>
    <div class="map" role="img" aria-label="Street map showing the route to the church"></div>
    <div class="text addr-name">Brookfield Fellowship High Desert</div>
    <div class="text addr-line">28315 Marigold Ave, Hesperia, Ca. 92345</div>
    <div class="text web">www.brookfieldfellowshipnt.com</div>
    <div class="text phone">555-317-4096</div>
  </section>
</main>
</body>
</html>
```